Two sided business card template for:

Nook 4 Keeps Storage
1873 Brindle Avenue,
Pinecrest, WK
S4R 2M6
306-517-3482
www.nook4keeps.ca

Front side should be standard business card information. Sample should be for Darren Kowalchuk, Operations Manager, darren@nook4keeps.ca

Back side should be an advertisement for the storage facility. Some points about our facility are below you may use some or all of these features in the ad.

-Online payments and bookings
-Seasonal bicycle, tire, and motorcycle storage
-24hr self storage access
-Safe, and secure, with digital video surveillance
-Airport location

Card could have, but doesn't need a clever tag line containing the company name

Finished design must be in Microsoft word, or publisher format, and text must be editable.

```html
<!DOCTYPE html>
<html lang="en">
<head>
<meta charset="utf-8">
<title>Nook 4 Keeps Storage – Business Card</title>
<link rel="stylesheet" href="https://fonts.googleapis.com/css2?family=Roboto:wght@400;700&display=swap">
<style>
  :root {
    --brand-red: #d0261f;
    --card-white: #ffffff;
    --ink-dark: #1f1f1f;
    --text-light: #ffffff;
    --backdrop: #e9e7e4;
    --card-shadow: rgba(0, 0, 0, 0.18);
  }
  * { margin: 0; padding: 0; box-sizing: border-box; }
  html, body {
    width: 1200px;
    height: 1000px;
    overflow: hidden;
    background: var(--backdrop);
    font-family: "Roboto", Arial, sans-serif;
  }
  .sheet {
    width: 1200px;
    height: 1000px;
    display: flex;
    flex-direction: column;
    align-items: center;
    justify-content: center;
    gap: 60px;
  }
  .card {
    position: relative;
    width: 700px;
    height: 400px;
    background: var(--brand-red);
    box-shadow: 0 6px 20px var(--card-shadow);
    overflow: hidden;
  }
  .card__shape {
    position: absolute;
    inset: 0;
    width: 100%;
    height: 100%;
  }
  .card__shape path { fill: var(--card-white); }

  .wordmark {
    position: absolute;
    display: flex;
    align-items: center;
    gap: 12px;
    font-weight: 700;
    font-size: 26px;
    line-height: 1.15;
    letter-spacing: 0.5px;
    text-transform: uppercase;
    color: var(--ink-dark);
  }
  .wordmark__mark {
    width: 34px;
    height: 34px;
    background: var(--brand-red);
    flex: none;
  }

  /* Front */
  .front .wordmark { top: 62px; left: 350px; width: 260px; }
  .address {
    position: absolute;
    top: 34px;
    left: 36px;
    color: var(--text-light);
    font-style: normal;
    font-size: 21px;
    line-height: 1.42;
  }
  .address__web { margin-top: 14px; }
  .contact {
    position: absolute;
    left: 400px;
    top: 292px;
    color: var(--text-light);
  }
  .contact__name { font-weight: 700; font-size: 27px; }
  .contact__role {
    margin-top: 6px;
    font-weight: 700;
    font-size: 15px;
    letter-spacing: 1px;
    text-transform: uppercase;
  }
  .contact__email {
    margin-top: 14px;
    font-size: 19px;
  }

  /* Back */
  .back .wordmark { top: 40px; left: 250px; }
  .features {
    position: absolute;
    left: 0;
    right: 0;
    top: 168px;
    list-style: none;
    text-align: center;
    color: var(--text-light);
    font-size: 22px;
    line-height: 1.45;
  }
</style>
</head>
<body>
<main class="sheet">

  <section class="card front" aria-label="Business card front">
    <svg class="card__shape" viewBox="0 0 700 400" preserveAspectRatio="none" aria-hidden="true">
      <path d="M250 0 C 330 150, 500 255, 700 275 L700 0 Z"/>
    </svg>
    <div class="wordmark"><span class="wordmark__mark"></span><span>Nook 4 Keeps<br>Storage</span></div>
    <address class="address">
      <div>Nook 4 Keeps Storage</div>
      <div>1873 Brindle Avenue,</div>
      <div>Pinecrest, WK</div>
      <div>S4R 2M6</div>
      <div>306-517-3482</div>
      <div class="address__web">www.nook4keeps.ca</div>
    </address>
    <div class="contact">
      <div class="contact__name">Darren Kowalchuk</div>
      <div class="contact__role">Operations Manager</div>
      <div class="contact__email">darren@nook4keeps.ca</div>
    </div>
  </section>

  <section class="card back" aria-label="Business card back">
    <svg class="card__shape" viewBox="0 0 700 400" preserveAspectRatio="none" aria-hidden="true">
      <path d="M0 0 H700 V80 C 520 110, 260 150, 0 150 Z"/>
    </svg>
    <div class="wordmark"><span class="wordmark__mark"></span>Nook 4 Keeps Storage</div>
    <ul class="features">
      <li>Online payments and bookings</li>
      <li>Seasonal bicycle, tire, and motorcycle storage</li>
      <li>24hr self storage access</li>
      <li>Safe, and secure, with digital video surveillance</li>
      <li>Airport location</li>
    </ul>
  </section>

</main>
</body>
</html>
```